Online shopping portal - Business Card Design

Brivanto.com.au is a complete shopping experience. Search, compare & buy items from partnered stores & receive cashbash for your purchases and referrals.
Mission
Our mission is to provide a system for entrepreneurs to create an ongoing income, while providing consumers worldwide with a better way to shop.
A product brokerage and Internet marketing company that specialises in One-to-One Marketing, Quelden Australia is a subsidiary of Quelden Norvik Worldwide, Inc.
With more than 3 million Preferred Customers and 180,000 Customer Managers worldwide, Quelden Norvik has generated over $3 billion USD in accumulated retail sales. The Company employs more than 675 people globally with international operations in Australia, United States, Canada, Taiwan, Hong Kong, Mexico & Singapore
Through revolutionary technology and the one-to-one marketing and social shopping Quelden Australia are leveraging the Internet with the power of people to create the economy of the future.
By providing online shoppers with the products and services they want and need — backed by the Company’s people power — Quelden Australia is fast becoming the World Wide Web’s ultimate online shopping destination.
As a result, we are changing the way people shop and changing the economic paradigm where anyone can become financially independent by creating their own economy — Rooted in Goods. Lifted by Folk®.
Description
Welcome to a new kind of comparison shopping site where you get PAID cashback to shop!
Simply create an account to start accumulating cash backs each time you make purchases across hundreds of trusted Partner Stores and thousands of your favorite brands through our convenient SwiftTote® for one stop shopping.
All merchant stores are backed by PELMARO.COM's 100% satisfaction guarantee.

Updates
Project Deadline Extended
Reason: Hi all,  I am extending the deadline as i'm going to be away for my birthday (and may not have time to check before the current deadline anyway)  I figure that the more time i give you the better.

Industry/Entity Type
Online Shopping
Contact Information for Business Card
Business Name: Brivanto.com.au
website: www.brivanto.com.au
Linkora: www.facebook.com/brivanto.com.au.
Email: info@brivanto.com.au
Phone: Mirel on 0497 28 14 56
Requirements
Nice to have
- Create a Brivanto logo

```html
<!DOCTYPE html>
<html lang="en">
<head>
<meta charset="utf-8">
<title>Brivanto.com.au – Business Card</title>
<link href="https://fonts.googleapis.com/css2?family=Arimo:wght@400;700&display=swap" rel="stylesheet">
<style>
  :root {
    --teal: #007f7a;
    --teal-light: #25b9c2;
    --white: #ffffff;
    --card-border: #b9e3e2;
    --label: #555555;
    --rule: #dddddd;
    --stage: #ecebea;
  }
  * { box-sizing: border-box; margin: 0; padding: 0; }
  html, body { width: 894px; height: 1200px; overflow: hidden; background: var(--white); }
  body { position: relative; font-family: "Arimo", Arial, sans-serif; }

  .swatch { position: absolute; top: 62px; width: 66px; height: 63px; }
  .swatch--light { left: 73px; background: var(--teal-light); }
  .swatch--dark { left: 145px; background: var(--teal); }
  .swatch-label { position: absolute; left: 70px; top: 136px; font-size: 12px; color: var(--label); }

  .card { position: absolute; width: 350px; height: 205px; text-align: center; }
  .card--front { background: var(--teal); color: var(--white); }
  .card--back { background: var(--white); border: 1px solid var(--card-border); color: var(--teal); }

  .brand-mark {
    position: absolute; left: 50%; top: 32px; width: 64px; height: 64px;
    margin-left: -32px; border-radius: 50%; border: 6px solid var(--white);
  }
  .card--back .brand-mark { top: 32px; width: 66px; height: 66px; margin-left: -33px; border-color: var(--teal); }
  .brand-name { position: absolute; left: 0; right: 0; top: 107px; font-size: 17px; font-weight: 700; }

  .actions { position: absolute; left: 0; right: 0; top: 140px; display: flex; justify-content: center; gap: 26px; }
  .action { width: 52px; display: flex; flex-direction: column; align-items: center; font-size: 11.5px; font-weight: 700; }
  .action svg { width: 28px; height: 26px; margin-bottom: 4px; }

  .tagline { position: absolute; left: 0; right: 0; top: 106px; font-size: 19px; font-weight: 700; }
  .contact { position: absolute; left: 0; right: 0; top: 133px; font-size: 8px; font-weight: 700; line-height: 10px; }
  .phone { position: absolute; left: 0; right: 0; top: 167px; font-size: 13px; font-weight: 700; }

  .divider { position: absolute; left: 80px; top: 559px; width: 727px; height: 1px; background: var(--rule); }
  .stage { position: absolute; left: 22px; top: 608px; width: 843px; height: 562px; background: var(--stage); }
</style>
</head>
<body>
  <div class="swatch swatch--light"></div>
  <div class="swatch swatch--dark"></div>
  <p class="swatch-label">Samples of teal ...</p>

  <div class="card card--front" style="left:261px; top:62px;">
    <div class="brand-mark"></div>
    <div class="brand-name">Brivanto.com.au</div>
    <div class="actions">
      <div class="action">
        <svg viewBox="0 0 28 26"><circle cx="12" cy="11" r="7" fill="none" stroke="#fff" stroke-width="3"/><line x1="17" y1="16" x2="23" y2="23" stroke="#fff" stroke-width="4" stroke-linecap="round"/></svg>Search
      </div>
      <div class="action">
        <svg viewBox="0 0 28 26"><path d="M5 9h18l-2 16H7z" fill="#fff"/><path d="M10 9V6a4 4 0 0 1 8 0v3" fill="none" stroke="#fff" stroke-width="2"/></svg>Compare
      </div>
      <div class="action">
        <svg viewBox="0 0 28 26"><rect x="4" y="7" width="20" height="15" rx="2" fill="none" stroke="#fff" stroke-width="3"/><line x1="4" y1="13" x2="24" y2="13" stroke="#fff" stroke-width="2"/></svg>Buy
      </div>
      <div class="action">
        <svg viewBox="0 0 28 26"><rect x="3" y="6" width="22" height="14" rx="1" fill="#fff"/><circle cx="14" cy="13" r="4" fill="var(--teal)"/></svg>Earn
      </div>
    </div>
  </div>

  <div class="card card--back" style="left:88px; top:305px;">
    <div class="brand-mark"></div>
    <div class="tagline">Get paid to shop</div>
    <div class="contact">Website: www.brivanto.com.au<br>Linkora: www.linkora.net/brivanto.com.au.<br>Email: info@brivanto.com.au</div>
    <div class="phone">0497 28 14 56</div>
  </div>

  <div class="card card--back" style="left:452px; top:305px;">
    <div class="brand-mark"></div>
    <div class="tagline">Get paid to shop</div>
    <div class="contact">Website: www.brivanto.com.au<br>Linkora: www.linkora.net/brivanto.com.au.<br>Email: info@brivanto.com.au</div>
    <div class="phone">0497 28 14 56</div>
  </div>

  <div class="divider"></div>

  <div class="stage">
    <div class="card card--front" style="left:48px; top:178px;">
      <div class="brand-mark"></div>
      <div class="brand-name">Brivanto.com.au</div>
      <div class="actions">
        <div class="action">
          <svg viewBox="0 0 28 26"><circle cx="12" cy="11" r="7" fill="none" stroke="#fff" stroke-width="3"/><line x1="17" y1="16" x2="23" y2="23" stroke="#fff" stroke-width="4" stroke-linecap="round"/></svg>Search
        </div>
        <div class="action">
          <svg viewBox="0 0 28 26"><path d="M5 9h18l-2 16H7z" fill="#fff"/><path d="M10 9V6a4 4 0 0 1 8 0v3" fill="none" stroke="#fff" stroke-width="2"/></svg>Compare
        </div>
        <div class="action">
          <svg viewBox="0 0 28 26"><rect x="4" y="7" width="20" height="15" rx="2" fill="none" stroke="#fff" stroke-width="3"/><line x1="4" y1="13" x2="24" y2="13" stroke="#fff" stroke-width="2"/></svg>Buy
        </div>
        <div class="action">
          <svg viewBox="0 0 28 26"><rect x="3" y="6" width="22" height="14" rx="1" fill="#fff"/><circle cx="14" cy="13" r="4" fill="var(--teal)"/></svg>Earn
        </div>
      </div>
    </div>

    <div class="card card--back" style="left:445px; top:178px;">
      <div class="brand-mark"></div>
      <div class="tagline">Get paid to shop</div>
      <div class="contact">Website: www.brivanto.com.au<br>Linkora: www.linkora.net/brivanto.com.au.<br>Email: info@brivanto.com.au</div>
      <div class="phone">0497 28 14 56</div>
    </div>
  </div>
</body>
</html>
```